Placing my newer logo on my existing business card

I have a business card that I had you guys do years ago, then I changed my logo, I love both my business card and my logo. The challenge is both my logo and my business card are very similar in color. So I'm not sure how to make my logo stand out.

Sick

```html
<!DOCTYPE html>
<html lang="en">
<head>
<meta charset="utf-8">
<title>Summit Wellness &amp; Hormone Studio – Business Card</title>
<link rel="stylesheet" href="https://fonts.googleapis.com/css2?family=Cinzel:wght@400;600;700&family=Lato:wght@400;700&family=Great+Vibes&display=swap">
<style>
  :root {
    --backdrop: #2e2e2e;
    --card: #ffffff;
    --rust: #ad4330;
    --teal: #7fa7ae;
    --ink: #3a3a3a;
    --photo-light: #ece9e6;
    --photo-dark: #6b6460;
  }
  * { box-sizing: border-box; margin: 0; padding: 0; }
  html, body {
    width: 1200px; height: 875px; overflow: hidden;
    background: var(--backdrop);
  }
  .canvas { position: relative; width: 1200px; height: 875px; }
  .card {
    position: absolute; left: 260px; width: 680px; height: 388px;
    background: var(--card); border-radius: 22px; overflow: hidden;
    box-shadow: 0 14px 40px rgba(0,0,0,.45);
  }
  .card--back { top: 34px; }
  .card--front { top: 453px; }

  /* Wordmark */
  .wordmark {
    font-family: "Cinzel", serif; font-weight: 600; color: var(--rust);
    letter-spacing: .06em; line-height: 1.05;
  }
  .brand-dot { display: inline-block; border-radius: 50%; background: var(--teal); }

  /* Back side */
  .back-content { position: absolute; inset: 0; z-index: 1; }
  .back-brand {
    position: absolute; left: 44px; top: 64px;
    display: flex; flex-direction: column; align-items: flex-start; gap: 10px;
  }
  .back-brand .brand-dot { width: 36px; height: 36px; margin-left: 60px; }
  .back-brand .wordmark { font-size: 20px; }
  .appointment {
    position: absolute; left: 44px; top: 170px; width: 330px;
    font-family: "Lato", sans-serif; color: var(--rust); font-size: 14px;
    letter-spacing: .06em;
  }
  .appointment__row { display: flex; align-items: flex-end; gap: 6px; height: 38px; }
  .appointment__line { flex: 1; border-bottom: 1.5px dotted var(--rust); margin-bottom: 4px; }
  .appointment__suffix { font-size: 12px; }
  .tagline {
    position: absolute; left: 72px; top: 280px;
    font-family: "Great Vibes", cursive; color: var(--rust); font-size: 38px;
    white-space: nowrap;
  }
  .portrait {
    position: absolute; right: 0; top: 0; width: 270px; height: 100%;
    background: linear-gradient(90deg, rgba(255,255,255,1) 0%, var(--photo-light) 22%, #cfc9c4 58%, var(--photo-dark) 100%);
  }

  /* Front side */
  .front-brand { position: absolute; left: 56px; top: 58px; }
  .front-brand .wordmark { font-size: 30px; }
  .front-mark { position: absolute; right: 58px; top: 40px; width: 200px; height: 200px; }
  .person { position: absolute; left: 56px; top: 160px; }
  .person__name {
    font-family: "Cinzel", serif; font-weight: 700; color: var(--rust);
    font-size: 26px; letter-spacing: .04em;
  }
  .person__role { font-family: "Lato", sans-serif; color: var(--teal); font-size: 17px; margin-top: 2px; }
  .accent-bar { position: absolute; left: 0; top: 190px; width: 12px; height: 40px; background: var(--teal); }
  .contacts {
    position: absolute; left: 56px; top: 232px; list-style: none;
    font-family: "Lato", sans-serif; color: var(--ink); font-size: 15px; line-height: 1.3;
  }
  .contacts li { display: flex; align-items: flex-start; gap: 10px; margin-bottom: 3px; }
  .contacts svg { width: 14px; height: 14px; margin-top: 3px; flex: none; fill: var(--rust); }
</style>
</head>
<body>
<main class="canvas">

  <section class="card card--back" aria-label="Card back">
    <div class="portrait" role="img" aria-label="Photo of a woman in a black sweater seated on a dark chair in a bright room"></div>
    <div class="back-content">
      <div class="back-brand">
        <span class="brand-dot"></span>
        <div class="wordmark">Summit Wellness<br>&amp; Hormone Studio</div>
      </div>
      <div class="appointment">
        <div class="appointment__row"><span>DATE</span><span class="appointment__line"></span></div>
        <div class="appointment__row"><span>TIME</span><span class="appointment__line"></span><span class="appointment__suffix">AM\PM</span></div>
      </div>
      <p class="tagline">Let's Make it Happen</p>
    </div>
  </section>

  <section class="card card--front" aria-label="Card front">
    <div class="front-brand">
      <div class="wordmark">Summit Wellness<br>&amp; Hormone Studio</div>
    </div>
    <span class="brand-dot front-mark"></span>
    <span class="accent-bar"></span>
    <div class="person">
      <div class="person__name">MARLA JENSEN</div>
      <div class="person__role">Director</div>
    </div>
    <ul class="contacts">
      <li>
        <svg viewBox="0 0 14 14"><path d="M7 0a5 5 0 0 0-5 5c0 3.6 5 9 5 9s5-5.4 5-9a5 5 0 0 0-5-5zm0 7a2 2 0 1 1 0-4 2 2 0 0 1 0 4z"/></svg>
        <span>1470 Harbor Ln Ste#2<br>Riverton, CO 80512</span>
      </li>
      <li>
        <svg viewBox="0 0 14 14"><path d="M3 1l2 .2 1 3-1.4 1.2a8 8 0 0 0 4 4L9.8 8l3 1 .2 2-1.5 1.8C6 12.5 1.5 8 1.2 2.5z"/></svg>
        <span>(555)214-7730</span>
      </li>
      <li>
        <svg viewBox="0 0 14 14"><path d="M3 1h6l2 2v3H3zM1 6h12v5h-2v2H3v-2H1zm3 3v3h6V9z"/></svg>
        <span>(555)214-7731</span>
      </li>
      <li>
        <svg viewBox="0 0 14 14"><path d="M1 3h12v8H1zm1 1v.4l5 3.2 5-3.2V4z"/></svg>
        <span>hello@summitwellnessstudio.com</span>
      </li>
      <li>
        <svg viewBox="0 0 14 14"><path d="M7 1a6 6 0 1 0 0 12A6 6 0 0 0 7 1zm0 1.3c.7.8 1.2 2.2 1.4 3.7H5.6C5.8 4.5 6.3 3.1 7 2.3zM2.4 7.3h2.2c.1 1.5.5 2.9 1.1 4A4.7 4.7 0 0 1 2.4 7.3zm0-1.3a4.7 4.7 0 0 1 3.3-3.7c-.6 1-1 2.300-1.1 3.7zm4.6 5.7c-.7-.8-1.2-2.2-1.4-3.7h2.8c-.2 1.5-.7 2.9-1.4 3.7zm1.3-.4c.6-1 1-2.4 1.1-4h2.2a4.7 4.7 0 0 1-3.3 4zM9.4 6c-.1-1.4-.5-2.7-1.1-3.7A4.7 4.7 0 0 1 11.6 6z"/></svg>
        <span>summitwellnessstudio.com</span>
      </li>
    </ul>
  </section>

</main>
</body>
</html>
```